Legal Service Estimated Retainer and Average Case Value

We need an 11x14 flyer that contains the standard retainers and average cost be case, both provided in documents, for each case type we handle. We need the information displayed, preferably in a way that makes the information readable but less troubling to a client shocked at price of litigation. We need one sheet with the retainers and average case value merged into one table.

Target Market(s)

Potential Clients

Font styles to use
Serif
Sans Serif

```html
<!DOCTYPE html>
<html lang="en">
<head>
<meta charset="utf-8">
<title>Retainers &amp; Average Fees by Case Type</title>
<link href="https://fonts.googleapis.com/css2?family=Fira+Sans:wght@400;600&display=swap" rel="stylesheet">
<style>
  :root {
    --page: #ffffff;
    --header: #626366;
    --ink: #232326;
    --navy: #141a3d;
    --white: #ffffff;
    --r1: #6cc58a;
    --r2: #33c0ef;
    --r3: #3fa9df;
    --r4: #4898d3;
    --r5: #4889c8;
    --r6: #4679bd;
    --r7: #446ab5;
    --r8: #4260ac;
    --r9: #435aa8;
    --r10: #4356a5;
    --r11: #6ec277;
    --r12: #6dc060;
    --r13: #6dbf47;
  }
  * { margin: 0; padding: 0; box-sizing: border-box; }
  html, body { width: 1200px; height: 943px; overflow: hidden; background: var(--page); }
  body { font-family: "Fira Sans", sans-serif; color: var(--ink); position: relative; }

  .fee-table {
    position: absolute;
    left: 110px; top: 79px;
    width: 978px;
  }
  .fee-row {
    display: grid;
    grid-template-columns: 326px 326px 326px;
    height: 51.3px;
    align-items: center;
    color: var(--white);
    font-size: 14.6px;
    line-height: 1.15;
  }
  .fee-row .case { padding-left: 5px; }
  .fee-row .retainer, .fee-row .average { text-align: center; }
  .fee-row .average { padding-left: 0; }
  .fee-head {
    background: var(--header);
    font-weight: 600;
    font-size: 17px;
    height: 51.6px;
  }
  .fee-head .case { text-align: center; padding-left: 0; }

  .row-1 { background: var(--r1); }
  .row-2 { background: var(--r2); }
  .row-3 { background: var(--r3); }
  .row-4 { background: var(--r4); }
  .row-5 { background: var(--r5); }
  .row-6 { background: var(--r6); }
  .row-7 { background: var(--r7); }
  .row-8 { background: var(--r8); }
  .row-9 { background: var(--r9); }
  .row-10 { background: var(--r10); }
  .row-11 { background: var(--r11); }
  .row-12 { background: var(--r12); }
  .row-13 { background: var(--r13); }

  .disclaimer {
    position: absolute;
    left: 110px; top: 828px;
    width: 640px;
    font-size: 14.6px;
    line-height: 17.4px;
    color: var(--ink);
  }
  .firm {
    position: absolute;
    left: 789px; top: 833px;
    display: flex;
    align-items: center;
    gap: 12px;
  }
  .firm-mark { width: 40px; height: 40px; background: var(--navy); }
  .firm-name {
    font-size: 17px;
    font-weight: 600;
    color: var(--navy);
    line-height: 1.2;
  }
</style>
</head>
<body>
  <div class="fee-table">
    <div class="fee-row fee-head">
      <div class="case">Case type</div>
      <div class="retainer">Retainers &amp; Estimated Case Cost</div>
      <div class="average">Average Fee Per Case Type</div>
    </div>
    <div class="fee-row row-1"><div class="case">(PTA) Protection from Abuse</div><div class="retainer">$2,000&nbsp; (Paid in full)</div><div class="average">$1,500 - $3,000</div></div>
    <div class="fee-row row-2"><div class="case">Divorce (3301 C)</div><div class="retainer">$2,000</div><div class="average">$1,500 - $3,000</div></div>
    <div class="fee-row row-3"><div class="case">Divorce (3301 D)</div><div class="retainer">$2,500</div><div class="average">$2,000 - $3,000</div></div>
    <div class="fee-row row-4"><div class="case">Divorce &amp; Support</div><div class="retainer">$3,000</div><div class="average">$2,000 - $4,000</div></div>
    <div class="fee-row row-5"><div class="case">Divorce &amp; Custody</div><div class="retainer">$3,500</div><div class="average">$5,000 - $8,000</div></div>
    <div class="fee-row row-6"><div class="case">Divorce &amp; Equitable Distribution</div><div class="retainer">$3,500</div><div class="average">$6,000 - $10,000</div></div>
    <div class="fee-row row-7"><div class="case">Divorce, Custody &amp; Support</div><div class="retainer">$3,500</div><div class="average">$8,000 - $12,000</div></div>
    <div class="fee-row row-8"><div class="case">Divorce, Equitable Distribution &amp; Support</div><div class="retainer">$3,500</div><div class="average">$8,000 - $12,000</div></div>
    <div class="fee-row row-9"><div class="case">Divorce, Equitable Distribution &amp; Custody</div><div class="retainer">$5,000</div><div class="average">$10,000 - $15,000</div></div>
    <div class="fee-row row-10"><div class="case">Divorce, Equitable Distribution, Custody<br>&amp; Support</div><div class="retainer">$3,500</div><div class="average">$12,000 - $15,000</div></div>
    <div class="fee-row row-11"><div class="case">Custody Initial Order</div><div class="retainer">$3,000</div><div class="average">$4,000 - $7,000</div></div>
    <div class="fee-row row-12"><div class="case">Custody &amp; Support</div><div class="retainer">$3,000</div><div class="average">$5,000 - $8,000</div></div>
    <div class="fee-row row-13"><div class="case">Custody Modification</div><div class="retainer">$3,500</div><div class="average">$5,000 - $8,000</div></div>
  </div>

  <p class="disclaimer">In order for our clients to set expectations for legal fees, we provide the national average range of fees per case type. These are only to provide you with an understanding of what other cases have cost clients in similar cases. Please note these are not estimates nor guarantees of your own legal costs.</p>

  <div class="firm">
    <div class="firm-mark"></div>
    <div class="firm-name">The Law Office of<br>Marcus T Hollander</div>
  </div>
</body>
</html>
```